Business Card Design needed for start up company Pramora

In need of a new business card designed for a start up company based in Sydney, Pramora is a new start up innovative Company, our mission it to make property accessible for everyday Australian and to become the leading Real Estate platform in Australia. We want it to be fresh and clean.

Industry/Entity Type

Financial

Contact Information for Business Card

Section for Name
Section for Title

PRAMORA - Where Doors Open Wide
Mobile:
Direct:

Font styles to use
Sans Serif

Colors
33a6d7
0692cd
0255a3
ffffff

Requirements
Must have
• Logo, all business card details

```html
<!DOCTYPE html>
<html lang="en">
<head>
<meta charset="utf-8">
<title>Pramora Business Card</title>
<link rel="stylesheet" href="https://fonts.googleapis.com/css2?family=Roboto+Condensed:ital,wght@0,300;0,400;0,700;0,800;1,300;1,700&display=swap">
<style>
  :root {
    --sky: #33a6d7;
    --ocean: #0692cd;
    --royal: #0255a3;
    --navy: #1d4a82;
    --white: #ffffff;
    --ink: #4a4f57;
    --page: #eef0f2;
  }
  * { margin: 0; padding: 0; box-sizing: border-box; }
  html, body { width: 1200px; height: 1200px; overflow: hidden; }
  body {
    background: var(--page);
    font-family: "Roboto Condensed", sans-serif;
    display: flex;
    flex-direction: column;
    align-items: center;
    justify-content: center;
    gap: 60px;
  }
  .card {
    position: relative;
    width: 900px;
    height: 514px;
    overflow: hidden;
    box-shadow: 0 6px 22px rgba(0,0,0,0.14);
  }
  .card-art { position: absolute; inset: 0; width: 100%; height: 100%; }

  /* Front */
  .card-front { background: var(--white); }
  .brand {
    position: absolute;
    left: 330px;
    top: 70px;
    display: flex;
    align-items: center;
    gap: 14px;
  }
  .brand-dot {
    width: 58px; height: 58px;
    border-radius: 50%;
    background: var(--ocean);
  }
  .brand-name {
    font-weight: 800;
    font-size: 64px;
    letter-spacing: 1px;
    color: var(--royal);
    line-height: 1;
  }
  .person { position: absolute; left: 332px; top: 168px; }
  .person-name {
    font-weight: 700;
    font-style: italic;
    font-size: 34px;
    color: var(--ocean);
    letter-spacing: 1px;
  }
  .person-title {
    font-size: 18px;
    font-style: italic;
    color: var(--ink);
    margin-top: 2px;
  }
  .contact {
    position: absolute;
    left: 520px;
    top: 320px;
    font-size: 20px;
    color: var(--ink);
    line-height: 1.45;
  }
  .contact-label { font-weight: 700; color: var(--royal); display: inline-block; width: 30px; }
  .contact-rule {
    width: 300px;
    height: 2px;
    background: var(--sky);
    margin: 10px 0 8px;
  }
  .contact-address { font-size: 20px; }

  /* Back */
  .card-back { background: linear-gradient(120deg, var(--ocean) 0%, #2f86bf 60%, #3a7fb2 100%); }
  .tagline-block { position: absolute; left: 170px; top: 120px; color: var(--white); }
  .tagline-brand { font-weight: 800; font-size: 52px; letter-spacing: 1px; line-height: 1; }
  .tagline-text { font-weight: 300; font-size: 44px; margin-top: 6px; }
</style>
</head>
<body>

<section class="card card-front" aria-label="Business card front">
  <svg class="card-art" viewBox="0 0 900 514" aria-hidden="true">
    <path d="M0,0 H190 Q95,260 255,514 H0 Z" fill="var(--navy)"/>
    <path d="M222,-4 Q128,260 290,518" fill="none" stroke="var(--ocean)" stroke-width="16"/>
  </svg>
  <div class="brand">
    <span class="brand-dot"></span>
    <span class="brand-name">PRAMORA</span>
  </div>
  <div class="person">
    <div class="person-name">JOHN DOE</div>
    <div class="person-title">Director</div>
  </div>
  <div class="contact">
    <div><span class="contact-label">T :</span>1-234-567890</div>
    <div><span class="contact-label">W :</span>www.pramora.com</div>
    <div><span class="contact-label">E :</span>john@pramora.com</div>
    <div class="contact-rule"></div>
    <div class="contact-address">Dummy city, Dummy Country Land</div>
  </div>
</section>

<section class="card card-back" aria-label="Business card back">
  <svg class="card-art" viewBox="0 0 900 514" aria-hidden="true">
    <path d="M300,514 Q690,500 900,330 V514 Z" fill="var(--white)"/>
    <path d="M330,514 Q700,515 900,352 V514 Z" fill="var(--sky)"/>
    <path d="M350,514 Q710,520 900,362 V514 Z" fill="#2c4a75"/>
  </svg>
  <div class="tagline-block">
    <div class="tagline-brand">PRAMORA</div>
    <div class="tagline-text">where doors open wide</div>
  </div>
</section>

</body>
</html>
```